Wedding Invitations

We are a printing company "inkmorrow" and require multiple wedding invitation designs for our customers in store and online. We would like the designs to be editable in Photoshop if possible, if not then a layout with suggested fonts would be the next best option. We are open to suggestions on design but would like to stick to the general wedding themes some with a modern and some with a classical feel

Industry/Entity Type

Printing

```html
<!DOCTYPE html>
<html lang="en">
<head>
<meta charset="utf-8">
<title>Wedding Invitation</title>
<link href="https://fonts.googleapis.com/css2?family=Abril+Fatface&family=Roboto+Slab:wght@300;400&family=Petit+Formal+Script&display=swap" rel="stylesheet">
<style>
  :root {
    --paper: #fdf3e3;
    --ink: #1f3b50;
    --ink-faint: #e9dfd0;
    --tile: #ecdcc3;
  }
  * { margin: 0; padding: 0; box-sizing: border-box; }
  html, body { width: 805px; height: 1200px; overflow: hidden; background: var(--paper); }
  .invitation {
    position: relative;
    width: 805px;
    height: 1200px;
    background: var(--paper);
    color: var(--ink);
    font-family: "Roboto Slab", serif;
  }
  .ornament-area {
    position: absolute;
    left: 250px; top: 54px;
    width: 305px; height: 80px;
    background: var(--ink-faint);
    border-radius: 40px;
  }
  .tile-area {
    position: absolute;
    width: 148px; height: 160px;
    background: var(--tile);
  }
  .tile-area--left { left: 107px; top: 107px; }
  .tile-area--right { left: 553px; top: 107px; }
  .rule { position: absolute; left: 156px; width: 494px; height: 0; border-top: 3px solid var(--ink); }
  .rule--thin { border-top-width: 1.5px; }
  .headline {
    position: absolute;
    left: 0; right: 0;
    display: block;
    text-align: center;
    font-family: "Abril Fatface", serif;
    font-weight: 400;
    line-height: 1;
  }
  .headline--were { top: 318px; font-size: 104px; letter-spacing: 30px; padding-left: 30px; }
  .headline--getting { top: 412px; font-size: 104px; letter-spacing: 1px; }
  .headline--married { top: 503px; font-size: 102px; letter-spacing: 1px; }
  .line { position: absolute; left: 0; right: 0; text-align: center; line-height: 1.2; }
  .script { font-family: "Petit Formal Script", cursive; font-size: 32px; }
  .detail { font-size: 26px; font-weight: 300; letter-spacing: 0.5px; text-transform: uppercase; }
  .joiner { font-size: 20px; font-weight: 400; letter-spacing: 1px; }
  .footer-rule { position: absolute; left: 155px; width: 495px; border-top: 1.5px solid var(--ink); }
  .reception { font-size: 26px; }
  .site { font-size: 22px; font-weight: 400; letter-spacing: 1px; }
</style>
</head>
<body>
<main class="invitation">
  <div class="ornament-area" role="img" aria-label="Decorative string with a looped heart joining the two letter tiles"></div>
  <div class="tile-area tile-area--left" role="img" aria-label="Illustrated letter tile with the first initial"></div>
  <div class="tile-area tile-area--right" role="img" aria-label="Illustrated letter tile with the second initial"></div>

  <div class="rule" style="top:308px"></div>
  <div class="rule rule--thin" style="top:316px"></div>

  <h1>
    <span class="headline headline--were">WE'RE</span>
    <span class="headline headline--getting">GETTING</span>
    <span class="headline headline--married">MARRIED</span>
  </h1>

  <div class="rule rule--thin" style="top:606px"></div>
  <div class="rule" style="top:614px"></div>

  <p class="line script" style="top:662px">Clara van Westerhout</p>
  <p class="line joiner" style="top:733px">AND</p>
  <p class="line script" style="top:770px">Miles Hartigan</p>

  <p class="line detail" style="top:855px">Friday 21st March 2014</p>
  <p class="line detail" style="top:890px">Four Thirty in the Afternoon</p>

  <p class="line detail" style="top:962px">Larkspur Restaurant,</p>
  <p class="line detail" style="top:997px">Wattlebrook, NSW</p>

  <div class="footer-rule" style="top:1063px"></div>
  <p class="line script reception" style="top:1080px">Cocktail Reception to follow,</p>
  <p class="line site" style="top:1138px">CLARAANDMILES.COM</p>
</main>
</body>
</html>
```